Design some Business Cards

need some business cards made up including my logo and details for scuba diving equipment business, business cards need to have the following details email:gord@[url removed, login to view],Bali mobile number +62 081379254061 Australia mobile no:+61 0473618204,name is GORDON KL PRATT, DIRECTOR. CARDS CAN BE IN BLACK OR WHITE BACKING,LOGO LOOKS GOOD WITH BOTH!Company address is [url removed, login to view] SARI VII NO.4 KEBUN ASRI [url removed, login to view],KECAMATAN KUTA SELATAN BANDUNG BALI 80517.

```html
<!DOCTYPE html>
<html lang="en">
<head>
<meta charset="utf-8">
<title>Tidepoint Gear – Business Cards</title>
<link rel="stylesheet" href="https://fonts.googleapis.com/css2?family=Questrial&family=Lato:wght@400;700&display=swap">
<style>
  :root {
    --bg-light: #8a8a8a;
    --bg-dark: #4a4a4a;
    --card-black: #151515;
    --card-white: #ffffff;
    --brand-blue: #1f8fd0;
    --brand-green: #8fae2a;
    --brand-yellow: #f2c21b;
    --ink: #2a2a2a;
    --rule: #444444;
  }
  * { margin: 0; padding: 0; box-sizing: border-box; }
  html, body { width: 1200px; height: 1200px; overflow: hidden; }
  body {
    background: radial-gradient(circle at 50% 45%, var(--bg-light), var(--bg-dark) 85%);
    position: relative;
    font-family: "Lato", sans-serif;
  }
  .card {
    position: absolute;
    left: 170px;
    width: 860px;
    height: 491px;
    border-radius: 26px;
    overflow: hidden;
    box-shadow: 0 18px 40px rgba(0,0,0,0.45);
  }
  .card--back { top: 70px; background: var(--card-black); }
  .card--front { top: 640px; background: var(--card-white); }

  .brand {
    position: absolute;
    font-family: "Questrial", sans-serif;
    font-size: 46px;
    letter-spacing: 1px;
    color: var(--brand-green);
    white-space: nowrap;
  }
  .card--back .brand { left: 50%; top: 50%; transform: translate(-50%, -50%); }
  .card--front .brand { left: 70px; top: 210px; font-size: 40px; }

  .contact {
    position: absolute;
    left: 470px;
    top: 70px;
    padding-left: 22px;
    border-left: 2px solid var(--rule);
    height: 150px;
  }
  .contact__name {
    font-family: "Questrial", sans-serif;
    font-size: 21px;
    color: var(--brand-green);
    letter-spacing: 1px;
  }
  .contact__role { font-size: 15px; color: var(--ink); margin: 4px 0 12px; }
  .contact__list { list-style: none; }
  .contact__item {
    display: flex; align-items: center; gap: 10px;
    font-size: 16px; color: var(--ink); line-height: 24px;
  }
  .contact__item svg { width: 16px; height: 16px; flex: none; }

  .footer-band {
    position: absolute; left: 0; bottom: 0;
    width: 100%; height: 110px;
  }
</style>
</head>
<body>
  <section class="card card--back" aria-label="Card back">
    <p class="brand">Tidepoint Gear</p>
  </section>

  <section class="card card--front" aria-label="Card front">
    <p class="brand">Tidepoint Gear</p>

    <div class="contact">
      <p class="contact__name">GORDON KL PRATT</p>
      <p class="contact__role">Director</p>
      <ul class="contact__list">
        <li class="contact__item">
          <svg viewBox="0 0 16 16"><path d="M3 1l3 3-1.5 2a9 9 0 0 0 5.5 5.5L12 10l3 3-2 2C7 15 1 9 1 3z" fill="var(--brand-green)"/></svg>
          +62 081379254061
        </li>
        <li class="contact__item">
          <svg viewBox="0 0 16 16"><rect x="4" y="1" width="8" height="14" rx="1.5" fill="none" stroke="var(--brand-yellow)" stroke-width="1.6"/></svg>
          +61 0473618204
        </li>
        <li class="contact__item">
          <svg viewBox="0 0 16 16"><rect x="1" y="3" width="14" height="10" fill="var(--brand-blue)"/><path d="M1 3l7 6 7-6" fill="none" stroke="#fff" stroke-width="1.3"/></svg>
          gord@tidepointgear.com
        </li>
        <li class="contact__item">
          <svg viewBox="0 0 16 16"><circle cx="8" cy="8" r="7" fill="var(--brand-yellow)"/><path d="M1 8h14M8 1c-3 3-3 11 0 14M8 1c3 3 3 11 0 14" fill="none" stroke="#fff" stroke-width="1"/></svg>
          www.tidepointgear.com
        </li>
      </ul>
    </div>

    <svg class="footer-band" viewBox="0 0 860 110" preserveAspectRatio="none">
      <path d="M0 18 L560 18 L600 0 L860 0 L860 110 L0 110 Z" fill="var(--card-black)"/>
      <path d="M560 18 L600 0 L640 0 L600 18 Z" fill="var(--brand-yellow)"/>
      <path d="M600 18 L640 0 L690 0 L650 18 Z" fill="var(--brand-green)"/>
    </svg>
  </section>
</body>
</html>
```